Need posters that inspire entrepreneurs

I want to create beautiful, inspiring wall art. I'm looking for a designer to create an awesome sample (note this sample is not for real use). The winning design will form the foundation of our art "style" so there will be LOTS of ongoing work for the winning designer.

It's your challenge to create a style that is clean, inspiring and timeless, and possibly can be adapted to different colour palettes.

Looking for a perfect execution of words, image and design.

The attached example shows one idea. It should serve as an idea only.

Format of the images should be either rectangular or square. Exact size is preferably UK A4 (US letter) or max A3. Assume that a display would consist of a 4 x 4 image grid so size needs to allow for that in a small to medium size office.

The quotes I want in the 3 samples (each in an individual poster - not combined in 1 poster). Each quote should have it's own, the reason for three is to prove the design work on more than one quote. The quotes are:

1) Failure is the condiment that gives success its flavor.
– Dorian Welsby

2) Whether you think you can or think you can’t, you’re right.
– Oswald Pike

3) Ever tried. Ever failed. No matter. Try Again. Fail again. Fail better.
– Lionel Marwick

Each design should include the image of the person and the quote + any design elements you consider relevant. You should find relevant images of the individuals being quoted. The final images will not be published or used commercially in any way.

Font styles to use
Serif
Sans Serif

Colors

Designer to choose colors to be used in the design.

Requirements
Must have
• Words and headshot image - 1 per poster design.
• Please consider in the design that there will not always be photographs of the person quoted and as such the design will need to hold, whether the source is a photo, sketch or something else.
Nice to have
• None, but note that the final image will be printed on a wall mounted board, printed to the edge but not on the edge. The board will have black or white edges so consider in the design.
Should not have
• None

```html
<!DOCTYPE html>
<html lang="en">
<head>
<meta charset="utf-8">
<title>Oswald Pike Quote Poster</title>
<link rel="stylesheet" href="https://fonts.googleapis.com/css2?family=Cinzel:wght@400;500&family=Great+Vibes&display=swap">
<style>
  :root {
    --edge: #ffffff;
    --ground: #130c09;
    --portrait-light: #9a7a63;
    --portrait-mid: #5a4030;
    --portrait-dark: #241812;
    --ink: #ffffff;
    --signature-tone: rgba(255, 255, 255, 0.10);
  }
  html, body {
    margin: 0;
    padding: 0;
    width: 1200px;
    height: 848px;
    overflow: hidden;
    background: var(--edge);
  }
  .poster {
    position: absolute;
    left: 15px;
    top: 13px;
    width: 1171px;
    height: 821px;
    background: var(--ground);
    overflow: hidden;
  }
  .portrait {
    position: absolute;
    left: 0;
    top: 0;
    width: 660px;
    height: 821px;
    background:
      radial-gradient(ellipse 300px 380px at 330px 390px,
        var(--portrait-light) 0%,
        var(--portrait-mid) 45%,
        var(--portrait-dark) 75%,
        var(--ground) 100%);
  }
  .quote {
    position: absolute;
    left: 657px;
    top: 80px;
    margin: 0;
    font-family: "Cinzel", "Times New Roman", serif;
    font-weight: 500;
    font-size: 58px;
    line-height: 77px;
    letter-spacing: 1px;
    color: var(--ink);
  }
  .quote span { display: block; white-space: nowrap; }
  .author {
    position: absolute;
    left: 622px;
    top: 565px;
    margin: 0;
    font-family: "Great Vibes", "Brush Script MT", cursive;
    font-weight: 400;
    font-size: 112px;
    line-height: 1;
    color: var(--ink);
    white-space: nowrap;
  }
  .signature {
    position: absolute;
    left: 844px;
    top: 700px;
    width: 305px;
    height: 88px;
    background: var(--signature-tone);
    border-radius: 4px;
  }
</style>
</head>
<body>
  <main class="poster">
    <div class="portrait" role="img" aria-label="Sepia headshot portrait of Oswald Pike"></div>
    <blockquote class="quote">
      <span>Whether</span>
      <span>you think</span>
      <span>you can</span>
      <span>or think</span>
      <span>you can’t,</span>
      <span>you’re right.</span>
    </blockquote>
    <p class="author">Oswald Pike</p>
    <div class="signature" role="img" aria-label="Handwritten signature of Oswald Pike"></div>
  </main>
</body>
</html>
```